New business card design needed for Diesel Fitting (Mechanical) Company

We need a new business card for our company called "Granite Valley Engineering" that showcases our logo and business details.
Target Market(s)
Owners of all makes and models of vehicles, trucks, plant and machinery.
Industry/Entity Type
Mechanical
Contact Information for Business Card
The business card details need to include the following: Owners/Directors: Trevor & Marisol Dunn-Calloway ABN: 47 913 206 781 Address: 561 Beaumont Street CHARTERS TOWERS QLD 4820 Postal Address: PO Box 8716 CHARTERS TOWERS QLD 4820 Website: www.gvengineering.com.au Phone: 4732 9185 Mobile: 0491 375 806 Emails: sales@gvengineering.com.au; admin@gvengineering.com.au; accounts@gvengineering.com.au; parts@gvengineering.com.au; office@gvengineering.com.au, reception@gvengineering.com.au
Look and feel

```html
<!DOCTYPE html>
<html lang="en">
<head>
<meta charset="utf-8">
<title>Granite Valley Engineering – Business Card</title>
<link rel="stylesheet" href="https://fonts.googleapis.com/css2?family=Open+Sans:wght@400;600&display=swap">
<style>
  :root {
    --backdrop: #e3e3e3;
    --card-dark: #323232;
    --card-light: #f4f4f4;
    --ink: #2e2e2e;
    --white: #ffffff;
    --red: #e2232b;
    --orange: #ec7123;
    --yellow: #f4b81c;
  }
  * { box-sizing: border-box; margin: 0; padding: 0; }
  html, body {
    width: 1200px; height: 960px; overflow: hidden;
    background: var(--backdrop);
    font-family: "Open Sans", Arial, sans-serif;
  }
  .canvas { position: relative; width: 1200px; height: 960px; }

  .card { position: absolute; left: 312px; width: 576px; height: 352px; }

  /* Back of card */
  .card-back { top: 110px; background: var(--card-dark); color: var(--white); }
  .card-back .brand {
    position: absolute; left: 0; right: 0; top: 232px; margin-top: -112px;
    display: flex; align-items: center; justify-content: center; gap: 14px;
  }
  .brand-dot { width: 22px; height: 22px; border-radius: 50%; background: var(--orange); flex: none; }
  .card-back .brand-name {
    font-size: 28px; font-weight: 600; color: var(--orange); letter-spacing: 0.2px;
  }
  .email-list {
    position: absolute; left: 0; right: 0; top: 293px;
    text-align: center; font-size: 12.6px; line-height: 20px; white-space: nowrap;
  }
  .email-list .sep { color: var(--yellow); padding: 0 3px; }
  .email-list .sep.muted { color: #bdbdbd; }

  /* Front of card */
  .card-front { top: 501px; height: 353px; background: var(--card-light); color: var(--ink); }
  .edge-stripe { position: absolute; left: 0; top: 0; width: 13px; height: 100%; }
  .edge-stripe span { position: absolute; left: 0; width: 13px; }
  .stripe-red-top { top: 0; height: 246px; background: var(--red); }
  .stripe-orange { top: 250px; height: 33px; background: var(--orange); }
  .stripe-yellow { top: 287px; height: 32px; background: var(--yellow); }
  .stripe-red-bottom { top: 323px; height: 30px; background: var(--red); }

  .card-front .brand {
    position: absolute; left: 53px; top: 66px;
    display: flex; align-items: center; gap: 12px;
  }
  .card-front .brand-name { font-size: 22px; font-weight: 600; color: var(--orange); }

  .owners { position: absolute; left: 52px; top: 175px; }
  .owners-name { font-size: 16.5px; font-weight: 600; color: var(--red); line-height: 22px; }
  .owners-role { font-size: 13.5px; line-height: 20px; }

  .contact { position: absolute; top: 245px; font-size: 13.5px; line-height: 19px; }
  .contact-phone { left: 52px; }
  .contact-address { left: 309px; }
  .contact li { list-style: none; display: flex; align-items: flex-start; }
  .contact .icon { width: 13px; height: 13px; margin: 3px 4px 0 0; flex: none; }
  .contact .label { color: var(--orange); margin-right: 4px; }
  .contact .indent { padding-left: 19px; }
</style>
</head>
<body>
<div class="canvas">

  <section class="card card-back">
    <div class="brand">
      <span class="brand-dot"></span>
      <span class="brand-name">Granite Valley Engineering</span>
    </div>
    <div class="email-list">
      <div>sales@gvengineering.com.au<span class="sep muted">|</span>admin@gvengineering.com.au<span class="sep">|</span>accounts@gvengineering.com.au</div>
      <div>parts@gvengineering.com.au<span class="sep">|</span>office@gvengineering.com.au<span class="sep">|</span>reception@gvengineering.com.au</div>
    </div>
  </section>

  <section class="card card-front">
    <div class="edge-stripe">
      <span class="stripe-red-top"></span>
      <span class="stripe-orange"></span>
      <span class="stripe-yellow"></span>
      <span class="stripe-red-bottom"></span>
    </div>

    <div class="brand">
      <span class="brand-dot"></span>
      <span class="brand-name">Granite Valley Engineering</span>
    </div>

    <div class="owners">
      <p class="owners-name">Trevor &amp; Marisol Dunn-Calloway</p>
      <p class="owners-role">Owners/Directors</p>
    </div>

    <ul class="contact contact-phone">
      <li>
        <svg class="icon" viewBox="0 0 16 16" aria-hidden="true"><path d="M3 1.5l2.5 0 1 3.5-1.6 1.2a9 9 0 0 0 4.9 4.9L11 9.5l3.5 1v2.5c0 .8-.7 1.5-1.5 1.5A12.5 12.5 0 0 1 1.5 3c0-.8.7-1.5 1.5-1.5z" fill="none" stroke="#e2232b" stroke-width="1.6"/></svg>
        <span>4732 9185</span>
      </li>
      <li>
        <svg class="icon" viewBox="0 0 16 16" aria-hidden="true"><rect x="4" y="1" width="8" height="14" rx="1.5" fill="none" stroke="#ec7123" stroke-width="1.5"/><circle cx="8" cy="12.3" r="0.9" fill="#ec7123"/></svg>
        <span>0491 375 806</span>
      </li>
      <li>
        <svg class="icon" viewBox="0 0 16 16" aria-hidden="true"><g fill="none" stroke="#ec7123" stroke-width="1.3"><circle cx="8" cy="8" r="6.5"/><ellipse cx="8" cy="8" rx="3" ry="6.5"/><path d="M1.5 8h13M2.5 4.7h11M2.5 11.3h11"/></g></svg>
        <span>www.gvengineering.com.au</span>
      </li>
      <li><span class="label">ABN:</span><span>47 913 206 781</span></li>
    </ul>

    <ul class="contact contact-address">
      <li>
        <svg class="icon" viewBox="0 0 16 16" aria-hidden="true"><path d="M2 7.5L8 2l6 5.5M3.5 6.5V14h9V6.5M6.5 14v-4h3v4" fill="none" stroke="#ec7123" stroke-width="1.4" stroke-linejoin="round"/></svg>
        <span>561 Beaumont Street</span>
      </li>
      <li class="indent">CHARTERS TOWERS QLD 4820</li>
      <li>
        <svg class="icon" viewBox="0 0 16 16" aria-hidden="true"><rect x="1.5" y="3.5" width="13" height="9" fill="none" stroke="#e2232b" stroke-width="1.4"/><path d="M1.5 3.5L8 9l6.5-5.5" fill="none" stroke="#e2232b" stroke-width="1.4"/></svg>
        <span>PO Box 8716</span>
      </li>
      <li class="indent">CHARTERS TOWERS QLD 4820</li>
    </ul>
  </section>

</div>
</body>
</html>
```